interior designer/stylist looking for a letter press business card to reflect the stylish work

Hello Designers,
I need a business card design for an company called Halvard Interior Design. I'm aiming at the high end residential and private client market in London providing sleek simple interiors. I'd like my business card to be tackboard worthy and expensive looking, i want people to pin it and for it to have a sought after look, and want prospective customers to hire me as their interior designer as my card is so beautiful.
I love letter press design. I also like the use of colour/foil on the edge.
Colour combos & general things I like -
Black and White
Navy Blue and Gold
Neutral colours (muted palette of greys whites navys beiges)
White Marble & brass
Morvane (fashion designer)
....also open to other suggestions....
Please dont take the pink in the attached photos too literally. i'd like the card to look more masculine than feminine.
I'd like Halvard on one side in one font, with interior design underneath so one word will make the statement....... unless anyone has any other ideas, open to suggestions.
I'd like a really simple font and for the whole card to look very graphic.
my details -
Petra Quillby
Interior Designer & Stylist
email petra@halvardinteriordesign.co.uk
phone +447813554019
website wwww.halvardinteriordesign.co.uk
GO GO GO!! EXCITED TO SEE THE OUTCOME!!
x L
Target Market(s)
High End Residential and private clients
Industry/Entity Type
Business
Contact Information for Business Card
Halvard Interior Design & Styling
Petra Quillby
phone +447813554019

```html
<!DOCTYPE html>
<html lang="en">
<head>
<meta charset="utf-8">
<title>Halvard Interior Design – Business Card</title>
<link rel="stylesheet" href="https://fonts.googleapis.com/css2?family=Source+Sans+3:wght@400;600;700&display=swap">
<style>
  :root {
    --stage: #e9e6e0;
    --card-yellow: #fcee2e;
    --card-navy: #10142f;
    --ink: #141414;
    --shadow: rgba(40, 30, 20, 0.22);
  }
  * { box-sizing: border-box; margin: 0; padding: 0; }
  html, body {
    width: 1200px;
    height: 900px;
    overflow: hidden;
    background: var(--stage);
    font-family: "Source Sans 3", "Myriad Pro", Arial, sans-serif;
  }
  .stage {
    position: relative;
    width: 1200px;
    height: 900px;
  }
  .card {
    position: absolute;
    left: 300px;
    width: 600px;
    height: 388px;
    background: var(--card-yellow);
    box-shadow: 0 10px 26px var(--shadow);
    overflow: hidden;
  }
  .card--front { top: 46px; }
  .card--back { top: 470px; }

  .wordmark {
    position: absolute;
    left: 0;
    right: 0;
    text-align: center;
    font-weight: 400;
    font-size: 44px;
    line-height: 1.1;
    letter-spacing: 0.5px;
  }
  .card--front .wordmark {
    top: 136px;
    color: var(--ink);
  }

  .band {
    position: absolute;
    left: 0;
    top: 0;
    width: 100%;
    height: 180px;
    background: var(--card-navy);
  }
  .band .wordmark {
    top: 42px;
    color: var(--card-yellow);
    font-size: 40px;
  }

  .contact {
    position: absolute;
    right: 28px;
    top: 198px;
    list-style: none;
    text-align: right;
    font-size: 15px;
    color: var(--ink);
  }
  .contact li {
    display: flex;
    justify-content: flex-end;
    align-items: center;
    gap: 8px;
    height: 22px;
  }
  .contact__icon {
    width: 15px;
    height: 15px;
    display: block;
  }

  .person {
    position: absolute;
    left: 36px;
    bottom: 38px;
    color: var(--ink);
  }
  .person__name {
    font-weight: 700;
    font-size: 24px;
    line-height: 1.2;
  }
  .person__role {
    font-weight: 400;
    font-size: 17px;
    margin-top: 4px;
    padding-left: 14px;
  }
</style>
</head>
<body>
<main class="stage">

  <section class="card card--front" aria-label="Business card front">
    <p class="wordmark">Halvard Interior<br>Design</p>
  </section>

  <section class="card card--back" aria-label="Business card back">
    <div class="band">
      <p class="wordmark">Halvard Interior<br>Design</p>
    </div>

    <ul class="contact">
      <li>+447813554019
        <svg class="contact__icon" viewBox="0 0 16 16" aria-hidden="true">
          <rect width="16" height="16" rx="2" fill="#10142f"/>
          <path d="M4 4.5c0-.5.4-1 1-1h1l1 2.3-1 1c.6 1.3 1.5 2.2 2.8 2.8l1-1 2.2 1v1c0 .6-.5 1-1 1C7.5 11.6 4 8.5 4 4.5z" fill="#fcee2e"/>
        </svg>
      </li>
      <li>petra@halvardinteriordesign.co.uk
        <svg class="contact__icon" viewBox="0 0 16 16" aria-hidden="true">
          <rect width="16" height="16" rx="2" fill="#10142f"/>
          <rect x="3.5" y="5" width="9" height="6.5" fill="none" stroke="#fcee2e" stroke-width="1.2"/>
          <path d="M3.5 5l4.5 3.6L12.5 5" fill="none" stroke="#fcee2e" stroke-width="1.2"/>
        </svg>
      </li>
      <li>wwww.halvardinteriordesign.co.uk
        <svg class="contact__icon" viewBox="0 0 16 16" aria-hidden="true">
          <rect width="16" height="16" rx="2" fill="#10142f"/>
          <path d="M7 9l2-2M6.2 7.6l-1.4 1.4a1.6 1.6 0 002.2 2.2l1.4-1.4M9.8 8.4l1.4-1.4a1.6 1.6 0 00-2.2-2.2L7.6 6.2" fill="none" stroke="#fcee2e" stroke-width="1.2" stroke-linecap="round"/>
        </svg>
      </li>
    </ul>

    <div class="person">
      <p class="person__name">Petra Quillby</p>
      <p class="person__role">Interior Designer &amp; Stylist</p>
    </div>
  </section>

</main>
</body>
</html>
```